We need letterhead, Business Cards, and envelops designed. We have attached a design of our logo and a sample of letterhead idea that was started but never perfected, it is only an idea for the letterhead if you can design something better we may love that also we are open to change.
We want a design that looks professional in style. we are a non profit trade association in the construction industry. the green color in the attached design represent green building, and we like that. also if you just want to enhance the letterhead sample that we attached that would be fine also.
Thanks and good luck
also the name that should show on the first business cards should be Merwin Haskell, Director are web address is www.vtqpa.org

```html
<!DOCTYPE html>
<html lang="en">
<head>
<meta charset="utf-8">
<title>VTQPA Envelope</title>
<link rel="stylesheet" href="https://fonts.googleapis.com/css2?family=Arimo:wght@400&display=swap">
<style>
  :root {
    --paper: #ffffff;
    --frame: #3a3a3a;
    --ink: #111111;
    --label-green: #2f6b2b;
    --value-grey: #7a7a7a;
    --accent-green: #4f8f3a;
    --wave-grey: #c9c9c9;
    --wave-green-light: #63a146;
    --wave-green-dark: #2f6a2a;
  }
  html, body {
    margin: 0;
    padding: 0;
    overflow: hidden;
    background: var(--paper);
  }
  .envelope {
    position: relative;
    width: 1200px;
    height: 600px;
    box-sizing: border-box;
    border: 1px solid var(--frame);
    background: var(--paper);
    overflow: hidden;
    font-family: "Arimo", Arial, sans-serif;
  }
  .brand {
    position: absolute;
    left: 78px;
    top: 52px;
    display: flex;
    align-items: center;
    gap: 16px;
  }
  .brand-mark {
    width: 26px;
    height: 26px;
    background: var(--accent-green);
  }
  .brand-name {
    font-size: 82px;
    line-height: 1;
    color: var(--ink);
    letter-spacing: 2px;
  }
  .contact {
    position: absolute;
    top: 511px;
    margin: 0;
    display: grid;
    grid-template-columns: auto auto;
    column-gap: 14px;
    row-gap: 3px;
    font-size: 13.6px;
    line-height: 16px;
  }
  .contact dt { color: var(--label-green); margin: 0; }
  .contact dd { color: var(--value-grey); margin: 0; }
  .contact-phone { left: 72px; }
  .contact-online { left: 322px; }
  .contact-address { left: 627px; }
  .corner-wave {
    position: absolute;
    left: 0;
    top: 0;
    width: 1200px;
    height: 600px;
  }
</style>
</head>
<body>
  <div class="envelope">
    <div class="brand">
      <span class="brand-name">VTQPA</span>
      <span class="brand-mark"></span>
    </div>

    <dl class="contact contact-phone">
      <dt>Tel.:</dt><dd>+01 23 4567 - 8900</dd>
      <dt>Fax:</dt><dd>+01 23 4567 - 8911</dd>
    </dl>

    <dl class="contact contact-online">
      <dt>Email:</dt><dd>merwin.haskell@vtqpa.org</dd>
      <dt>Web:</dt><dd>www.vtqpa.org</dd>
    </dl>

    <dl class="contact contact-address">
      <dt>Address:</dt><dd>1750 Linden Avenue</dd>
      <dt></dt><dd>Brookfield, ST 00000</dd>
    </dl>

    <svg class="corner-wave" viewBox="0 0 1200 600" role="img" aria-label="Decorative green and grey corner wave">
      <defs>
        <linearGradient id="wave-fill" x1="0" y1="0" x2="1" y2="0">
          <stop offset="0" stop-color="var(--wave-grey)"/>
          <stop offset="0.3" stop-color="var(--wave-green-light)"/>
          <stop offset="1" stop-color="var(--wave-green-dark)"/>
        </linearGradient>
      </defs>
      <path fill="url(#wave-fill)" d="M1200,0 C1150,160 980,330 982,600 L1200,600 Z"/>
    </svg>
  </div>
</body>
</html>
```